Quirk Pavilion home page design

I'd like to take quirkpavilion.example existing home page and use the logo attached and make and the home page look like brainwhimsy.example home page or endlesscub.example. The font size of the buttons should be similar to brainwhimsy.example. does this make sense?
I've added a mock up of the layout design. I'm looking for fun nerd like design on the left and right of the borders. It should be faint but visible and add more character to the site apart from just a solid black thick border. We'd like the Glasses to be a Favicon as well.
Getting better. Let's try the logo in the top middle of the page and make sure it is bigger than the banner to the left and right. Add maybe the search bar to the left and the shipping info to the right of the log pyramid. if you do this right the pyramid will look like a nose and the surrounding rectangles will look like the glasses inside the logo we have.
Can you make the robots look like the cosmic riddle cinema robots? They were the shadows of three robots at the bottom right of the tv show and they were watching movies and commenting on them. It may be a nice touch to have the robots looking at the site instead of at us the shopper from the bottom right.
Can you experiment with the side columns with what the inside of a temple may look like. Maybe some Egyptian columns with torches hanging from them.
Also can we try less pastel colors and more bold primary colors. Maybe experiment with Orange or a darker bolder blue?
Nice work. Also please correct spelling of "Customer" in the bar. And can you add a Q Glide feature in the middle above the products? this is where five featured products will rotate like a QGlide works
Reason: We have the holiday coming up and I guaranteed payment so we would like to see some quality work.
Target Market(s)
Target Market is young Moms, College Students and kids
Industry/Entity Type
Shipping
Look and feel
Each slider illustrates characteristics of the customer's brand and the style your logo design should communicate.

```html
<!DOCTYPE html>
<html lang="en">
<head>
<meta charset="utf-8">
<title>Quirk Pavilion</title>
<link rel="stylesheet" href="https://fonts.googleapis.com/css2?family=PT+Sans:wght@400;700&display=swap">
<style>
:root{
  --page-bg:#1d3e70;
  --panel:#ffffff;
  --brand-blue:#245594;
  --brand-blue-light:#336fb5;
  --brand-blue-dark:#1b467f;
  --heading-blue:#1f5599;
  --ink:#333333;
  --muted:#666666;
  --soft:#f1f1f1;
  --rule:#dddddd;
  --dark-btn:#444444;
}
*{box-sizing:border-box;margin:0;padding:0}
html,body{width:1050px;height:1200px;overflow:hidden}
body{background:var(--page-bg);font-family:"PT Sans",Arial,sans-serif;color:var(--ink);position:relative}
.abs{position:absolute}
.top-search{left:828px;top:13px;width:169px;height:24px;background:#fff;border:1px solid #ccc;border-radius:2px;font-size:11px;color:#aaa;font-style:italic;padding:5px 14px}
.top-search svg,.field svg{position:absolute;right:6px;top:6px}
.panel{left:45px;top:50px;width:960px;height:1072px;background:var(--panel);border-radius:3px}
.brand{left:55px;top:70px;display:flex;align-items:center;gap:8px}
.brand-mark{width:18px;height:18px;background:var(--ink)}
.brand-name{font-size:25px;font-weight:700;color:var(--ink);letter-spacing:.5px}
.utility{top:78px;right:55px;display:flex;gap:28px;font-size:13px;color:#444;align-items:center}
.utility span{display:flex;align-items:center;gap:8px}
.contact{top:125px;right:53px;font-size:17px;color:var(--heading-blue);display:flex;align-items:center;gap:10px}
.nav{left:53px;top:187px;width:945px;height:52px;background:linear-gradient(var(--brand-blue-light),var(--brand-blue-dark));border-radius:4px;display:flex;align-items:center}
.nav a{color:#fff;text-decoration:none;font-size:13px;height:52px;display:flex;align-items:center;padding:0 23px;border-right:1px solid #1a4277;box-shadow:1px 0 0 #3d78be}
.nav a.current{padding:0 34px}
.social{position:absolute;right:18px;top:11px;display:flex;gap:8px}
.social i{width:30px;height:30px;border-radius:50%;background:#fff;display:block}
.side-search{left:53px;top:258px;width:245px;height:67px;background:linear-gradient(var(--brand-blue-light),var(--brand-blue-dark));border-radius:3px 3px 0 0;color:#fff;font-size:12px;padding:9px 13px}
.field{position:absolute;background:#fff;border:1px solid #ccc;font-size:11px;font-style:italic;color:#aaa;padding:5px 14px}
.categories{left:53px;top:325px;width:245px;height:315px;background:var(--soft)}
.categories h2{font-size:15px;font-weight:400;color:var(--heading-blue);padding:15px 13px 10px;margin:0 11px 0 0;border-bottom:1px solid var(--rule)}
.categories ul{list-style:none;padding:12px 0 0 22px}
.categories li{font-size:12px;color:var(--muted);height:28px;display:flex;align-items:center;gap:11px}
.categories li::before{content:"";border-left:4px solid #888;border-top:3px solid transparent;border-bottom:3px solid transparent}
.slider{left:360px;top:260px;width:600px;height:300px;background:#fafafa;border:1px solid #eee;box-shadow:0 8px 14px rgba(0,0,0,.08);padding:16px}
.slider-photo{width:568px;height:268px;background:linear-gradient(120deg,#e43a4a,#f39a26 25%,#f0e04c 40%,#d54fb5 55%,#7ccf4a 70%,#2d8fe0 82%,#7f3ec4);border:1px solid #ddd}
.slide-arrow{width:42px;height:42px;border-radius:50%;background:#4a4a4a;top:390px;display:flex;align-items:center;justify-content:center}
.announce{left:318px;top:586px;width:679px;height:53px;background:#e9e9e9;font-size:13.5px;color:#555;padding:17px 26px}
.announce b{color:var(--heading-blue)}
.products-bar{left:69px;top:669px;width:648px;height:43px;background:var(--brand-blue);border-radius:3px;color:#fff;font-size:16px;padding:12px 16px}
.products-bar svg{position:absolute;right:16px;top:15px}
.product{width:126px}
.product-photo{width:126px;height:80px;border:2px solid #e6e6e6}
.product-name{font-size:12px;color:var(--muted);margin:11px 0 0 3px}
.product-price{font-size:12px;font-weight:700;color:var(--heading-blue);margin:5px 0 0 3px}
.cart-btn{margin:9px 0 0 3px;width:122px;height:27px;background:linear-gradient(var(--brand-blue-light),var(--brand-blue-dark));border-radius:3px;color:#fff;font-size:12px;display:flex;align-items:center;justify-content:center;gap:6px;box-shadow:0 1px 2px rgba(0,0,0,.3)}
.promo{left:738px;top:669px;width:250px;height:299px;background:linear-gradient(#9fbf7a,#c9a98a 50%,#111 78%)}
.newsletter{left:738px;top:983px;width:250px;height:117px;background:#ececec;border-bottom:2px solid #ccc}
.newsletter h2{font-size:16px;font-weight:400;color:var(--heading-blue);padding:13px 15px}
.submit{left:168px;top:87px;width:58px;height:21px;background:var(--dark-btn);color:#eee;font-size:11px;font-style:italic;text-align:center;line-height:21px}
.footer-links{top:1140px;left:0;width:1050px;text-align:center;font-size:12px;color:#dfe6f0}
.footer-links span{padding:0 8px}
.footer-links a{color:#dfe6f0;text-decoration:none}
.footer-links a.current{color:#fff}
.copyright{top:1170px;left:0;width:1050px;text-align:center;font-size:11px;color:#dfe6f0}
</style>
</head>
<body>
<div class="abs top-search">Search
  <svg width="10" height="10" viewBox="0 0 10 10"><circle cx="4" cy="4" r="3" fill="none" stroke="#aaa"/><path d="M6 6l3 3" stroke="#aaa"/></svg>
</div>
<div class="abs panel"></div>

<div class="abs brand"><i class="brand-mark"></i><span class="brand-name">Quirk Pavilion</span></div>

<div class="abs utility">
  <span><svg width="20" height="16" viewBox="0 0 20 16"><path d="M2 5h16l-2 10H4z" fill="#8aa3c0"/><path d="M6 5l4-4 4 4" stroke="#666" fill="none"/></svg>My Cart &nbsp; ( 0 ) Items &nbsp;- &nbsp;$ 0.00</span>
  <span><svg width="18" height="16" viewBox="0 0 18 16"><circle cx="9" cy="5" r="4" fill="#444"/><path d="M1 16c0-5 16-5 16 0z" fill="#444"/></svg>My Account</span>
  <span><svg width="16" height="18" viewBox="0 0 16 18"><rect x="1" y="2" width="14" height="16" fill="#444"/><path d="M4 7h8M4 10h8M4 13h8" stroke="#fff"/></svg>My Wish List</span>
</div>
<div class="abs contact">
  <svg width="16" height="16" viewBox="0 0 16 16"><path d="M3 1l3 3-2 2c1 2 3 4 5 5l2-2 3 3-2 3C7 15 1 9 1 3z" fill="var(--heading-blue)"/></svg>
  <span>Call Us : 555 014 2288 &nbsp; | &nbsp; Email : info@quirkpavilion.example</span>
</div>

<nav class="abs nav">
  <a class="current" href="#">Home</a><a href="#">About Us</a><a href="#">Our Products</a><a href="#">Shipping &amp; Returns</a><a href="#">RSS Syndication</a><a href="#">Contact Us</a>
  <div class="social"><i></i><i></i></div>
</nav>

<div class="abs side-search">Product Search
  <div class="field" style="left:13px;top:32px;width:220px;height:25px">Enter Product
    <svg width="10" height="10" viewBox="0 0 10 10"><circle cx="4" cy="4" r="3" fill="none" stroke="#aaa"/><path d="M6 6l3 3" stroke="#aaa"/></svg>
  </div>
</div>
<div class="abs categories">
  <h2>Product Categories</h2>
  <ul>
    <li>Nunc dictum vestibulum</li><li>Pellentesque auctor</li><li>Morbi mollis posuere</li>
    <li>Cras vitae odio vitae</li><li>Quisque eu ante</li><li>Cras viverra mi ac mauris</li>
    <li>Fusce non massa nec</li><li>Vestibulum blandit</li><li>Vivamus viverra odiosed</li>
  </ul>
</div>

<div class="abs slider"><div class="slider-photo" role="img" aria-label="Row of colourful translucent bendable figures with raised arms"></div></div>
<div class="abs slide-arrow" style="left:338px"><svg width="10" height="12"><path d="M7 1L2 6l5 5" stroke="#fff" stroke-width="2" fill="none"/></svg></div>
<div class="abs slide-arrow" style="left:950px"><svg width="10" height="12"><path d="M3 1l5 5-5 5" stroke="#fff" stroke-width="2" fill="none"/></svg></div>

<div class="abs announce"><b>Announcements :</b> Nunc ullamcorper lorem sed tincidunt leo eget sapien pretium at ultricies est fermentum.</div>

<div class="abs products-bar">Our Products
  <svg width="24" height="12"><path d="M6 1L1 6l5 5M18 1l5 5-5 5" stroke="#fff" stroke-width="2" fill="none"/></svg>
</div>

<div class="abs product" style="left:70px;top:727px"><div class="product-photo" role="img" aria-label="Key covers with cartoon faces in card packaging" style="background:linear-gradient(90deg,#d8d8d8,#e4d27a,#9ab6d8)"></div><p class="product-name">KeyGrins</p><p class="product-price">$10.75</p><div class="cart-btn">ADD TO CART <svg width="12" height="10"><path d="M1 1l4 4-4 4M6 1l4 4-4 4" stroke="#fff" stroke-width="2" fill="none"/></svg></div></div>
<div class="abs product" style="left:244px;top:727px"><div class="product-photo" role="img" aria-label="Key covers shaped like birds in card packaging" style="background:linear-gradient(90deg,#d9d9d9,#e7d04a,#cfcfcf)"></div><p class="product-name">KeyGrins</p><p class="product-price">$10.75</p><div class="cart-btn">ADD TO CART <svg width="12" height="10"><path d="M1 1l4 4-4 4M6 1l4 4-4 4" stroke="#fff" stroke-width="2" fill="none"/></svg></div></div>
<div class="abs product" style="left:417px;top:727px"><div class="product-photo" role="img" aria-label="Two pale bendable figures" style="background:linear-gradient(90deg,#e6e8e6,#bfe0c4,#a9d5e6)"></div><p class="product-name">KeyGrins</p><p class="product-price">$10.75</p><div class="cart-btn">ADD TO CART <svg width="12" height="10"><path d="M1 1l4 4-4 4M6 1l4 4-4 4" stroke="#fff" stroke-width="2" fill="none"/></svg></div></div>
<div class="abs product" style="left:591px;top:727px"><div class="product-photo" role="img" aria-label="Group of colourful bendable figures" style="background:linear-gradient(90deg,#e8506a,#f2b23a,#c56ad0,#4c9be0)"></div><p class="product-name">KeyGrins</p><p class="product-price">$10.75</p><div class="cart-btn">ADD TO CART <svg width="12" height="10"><path d="M1 1l4 4-4 4M6 1l4 4-4 4" stroke="#fff" stroke-width="2" fill="none"/></svg></div></div>

<div class="abs product" style="left:70px;top:928px"><div class="product-photo" role="img" aria-label="Red, orange and purple bendable figures" style="background:linear-gradient(90deg,#e34a5a,#f09a3a,#a05ac8)"></div><p class="product-name">KeyGrins</p><p class="product-price">$10.75</p><div class="cart-btn">ADD TO CART <svg width="12" height="10"><path d="M1 1l4 4-4 4M6 1l4 4-4 4" stroke="#fff" stroke-width="2" fill="none"/></svg></div></div>
<div class="abs product" style="left:244px;top:928px"><div class="product-photo" role="img" aria-label="Black bendable gadget with red coils" style="background:linear-gradient(90deg,#dcdcdc,#333,#c8343a)"></div><p class="product-name">KeyGrins</p><p class="product-price">$10.75</p><div class="cart-btn">ADD TO CART <svg width="12" height="10"><path d="M1 1l4 4-4 4M6 1l4 4-4 4" stroke="#fff" stroke-width="2" fill="none"/></svg></div></div>
<div class="abs product" style="left:417px;top:928px"><div class="product-photo" role="img" aria-label="Novelty desk gadgets on a corkboard" style="background:linear-gradient(90deg,#8a6a4a,#b8b8b8,#9c7a56)"></div><p class="product-name">KeyGrins</p><p class="product-price">$10.75</p><div class="cart-btn">ADD TO CART <svg width="12" height="10"><path d="M1 1l4 4-4 4M6 1l4 4-4 4" stroke="#fff" stroke-width="2" fill="none"/></svg></div></div>
<div class="abs product" style="left:591px;top:928px"><div class="product-photo" role="img" aria-label="Miniature wooden bowling lane with pins" style="background:linear-gradient(#f1f1f1 45%,#c99a62 60%,#a8783e)"></div><p class="product-name">KeyGrins</p><p class="product-price">$10.75</p><div class="cart-btn">ADD TO CART <svg width="12" height="10"><path d="M1 1l4 4-4 4M6 1l4 4-4 4" stroke="#fff" stroke-width="2" fill="none"/></svg></div></div>

<div class="abs promo" role="img" aria-label="Promotional banner for a running race series, showing a runner's legs above event dates"></div>

<div class="abs newsletter">
  <h2>Our Newsletter</h2>
  <div class="field" style="left:17px;top:48px;width:210px;height:29px;padding-top:8px">Enter your mail ID</div>
  <div class="abs submit">SUBMIT</div>
</div>

<div class="abs footer-links"><a class="current" href="#">Home</a><span>|</span><a href="#">About Us</a><span>|</span><a href="#">Our Products</a><span>|</span><a href="#">Shipping &amp; Returns</a><span>|</span><a href="#">RSS Syndication</a><span>|</span><a href="#">Contact Us</a></div>
<div class="abs copyright">Copyright © 2012 www.quirkpavilion.example &nbsp;&nbsp; All rights reserved.</div>
</body>
</html>
```